Duel Business card

Want an edgy business card that shows both of our companies on each side of the card, OR both together with a cool design.

*Must be edgy: We have attached our two business logos. We are a bail bond and immigration bond company.

Would like the address on one side only.
Need Phone, cell, website, address, and Name

Company Name 1: Cellgate Release Partners
www.cellgatereleasepartners.example

Company Name 2: Borderline Surety Associates
www.borderlinesuretyassociates.example

These cards will need to be easily changeable so I can modify new employees

Target Market(s)

people in jail, takign imigrants out of jail and from being taken back to there country

Industry/Entity Type

Business

Requirements
Must have
• Include both logos attached

```html
<!DOCTYPE html>
<html lang="en">
<head>
<meta charset="utf-8">
<title>Business Card – Front and Back</title>
<link rel="stylesheet" href="https://fonts.googleapis.com/css2?family=Arimo:wght@400;700&display=swap">
<style>
  :root {
    --stage: #b3b3b3;
    --navy: #033087;
    --red: #e53226;
    --gold: #f2c313;
    --white: #ffffff;
    --ink: #222222;
    --paper-light: #ffffff;
    --paper-shade: #d9d9d9;
  }
  * { margin: 0; padding: 0; box-sizing: border-box; }
  html, body { width: 1200px; height: 602px; overflow: hidden; }
  body {
    background: var(--stage);
    font-family: "Arimo", Arial, sans-serif;
    position: relative;
  }
  .card { position: absolute; width: 509px; height: 307px; overflow: hidden; }

  /* Front */
  .card-front { left: 56px; top: 56px; background: var(--red); }
  .card-front .split { position: absolute; inset: 0; }
  .brand-left {
    position: absolute; left: 20px; top: 112px; width: 220px;
    display: flex; flex-direction: column; align-items: center; gap: 10px;
  }
  .brand-left .dot { width: 44px; height: 44px; border-radius: 50%; background: var(--gold); }
  .brand-left .name {
    color: var(--white); font-weight: 700; font-size: 17px;
    text-align: center; line-height: 1.15; letter-spacing: 0.5px;
  }
  .brand-right {
    position: absolute; left: 312px; top: 76px; width: 156px; height: 156px;
    border-radius: 50%; background: var(--white);
    display: flex; align-items: center; justify-content: center; text-align: center;
    padding: 18px;
  }
  .brand-right .name { color: var(--navy); font-weight: 700; font-size: 15px; line-height: 1.2; }

  /* Back */
  .card-back {
    left: 634px; top: 238px;
    background: linear-gradient(100deg, var(--paper-light) 40%, var(--paper-shade) 100%);
  }
  .card-back .bands { position: absolute; inset: 0; }
  .person-name {
    position: absolute; left: 28px; top: 52px;
    color: var(--navy); font-weight: 700; font-size: 25px;
  }
  .name-rule { position: absolute; left: 28px; top: 83px; width: 454px; height: 3px; display: flex; }
  .name-rule span:first-child { flex: 0 0 227px; background: var(--red); }
  .name-rule span:last-child { flex: 1; background: var(--navy); }

  .office { position: absolute; left: 28px; display: flex; align-items: flex-start; }
  .office-one { top: 114px; }
  .office-two { top: 200px; }
  .office .mark {
    width: 70px; display: flex; justify-content: center; padding-top: 10px;
  }
  .office .mark span { display: block; width: 46px; height: 46px; border-radius: 50%; }
  .office-one .mark span { background: var(--navy); }
  .office-two .mark span { background: var(--white); border: 2px solid var(--paper-shade); }
  .office .details { margin-left: 26px; font-size: 14px; line-height: 16.5px; color: var(--ink); }
  .office .company { font-weight: 700; font-size: 14px; }
  .office-one .company { color: var(--navy); }
  .office-two .company { color: var(--red); }
  .office .label { font-weight: 700; font-style: italic; }
</style>
</head>
<body>

<section class="card card-front" aria-label="Card front">
  <svg class="split" width="509" height="307" viewBox="0 0 509 307" aria-hidden="true">
    <polygon points="0,0 295,0 250,151 260,153 216,307 0,307" fill="var(--navy)"/>
  </svg>
  <div class="brand-left">
    <span class="dot"></span>
    <p class="name">CELLGATE RELEASE PARTNERS</p>
  </div>
  <div class="brand-right">
    <p class="name">BORDERLINE SURETY ASSOCIATES</p>
  </div>
</section>

<section class="card card-back" aria-label="Card back">
  <svg class="bands" width="509" height="307" viewBox="0 0 509 307" aria-hidden="true">
    <polygon points="0,0 293,0 286,28 0,28" fill="var(--navy)"/>
    <polygon points="224,280 509,280 509,307 216,307" fill="var(--red)"/>
  </svg>

  <h1 class="person-name">Daniel Verrick</h1>
  <div class="name-rule"><span></span><span></span></div>

  <div class="office office-one">
    <div class="mark"><span></span></div>
    <div class="details">
      <p class="company">Cellgate Release Partners Las Vegas</p>
      <p>418 N. Harbor Point Ave. Las Vegas, NV 89101</p>
      <p><span class="label">t</span>. 1-888-555-0142 &nbsp; <span class="label">m</span>. 775-555-0187</p>
      <p>www.cellgatereleasepartners.example</p>
    </div>
  </div>

  <div class="office office-two">
    <div class="mark"><span></span></div>
    <div class="details">
      <p class="company">Borderline Surety Associates Agency, LLC.</p>
      <p>418 N. Harbor Point Ave. Las Vegas, NV 89101</p>
      <p><span class="label">t</span>. 877-555-0163 &nbsp; <span class="label">m</span>. 775-555-0187</p>
      <p>www.borderlinesuretyassociates.example</p>
    </div>
  </div>
</section>

</body>
</html>
```